Robotic startup business cards

We are looking for a design for a set of business cards which reflect the spirit and humor of Vortalo Robotics. We want to present ourselves as sleek, professional, but laid-back consulting company.

We primarily focus on developing robotic arms software. This software controls robots and does things like grab items, pick objects up, move them, etc.

We want to allow you maximum design creativity, but do ask that you consider our existing style guidelines (see attached files) in order to make our brand cohesive.

Target Market(s)

Startups and Mid-size robotic companies

Industry/Entity Type

Business

Contact Information for Business Card

Miro Halvensky, PhD
Roboticist | Vortalo Consulting | 318.570.9164

Font styles to use
Other font styles liked:
• Source code pro

Requirements
Must have
• robots or robotic arms
• similar color scheme that works with existing brand guidelines
Nice to have
• please consider our existing style guidelines (see attached files) in order to make our brand cohesive.
• minimalism style is generally nice.
Should not have
• An old, boring, or corporate feel. Too much text.

```html
<!DOCTYPE html>
<html lang="en">
<head>
<meta charset="utf-8">
<title>Vortalo Robotics Business Cards</title>
<link rel="stylesheet" href="https://fonts.googleapis.com/css2?family=Source+Sans+3:wght@400;500&display=swap">
<style>
  :root {
    --backdrop: #bcbcbc;
    --card-white: #f1f1f1;
    --ink: #2a2a2a;
    --ink-soft: #3a3a3a;
    --brand-green: #05d18f;
    --brand-green-deep: #02bf82;
    --card-shadow: 0 3px 6px rgba(0, 0, 0, 0.28);
  }
  * { margin: 0; padding: 0; box-sizing: border-box; }
  html, body {
    width: 1200px;
    height: 576px;
    overflow: hidden;
    background: var(--backdrop);
    font-family: "Source Sans 3", "Source Sans Pro", sans-serif;
  }
  .canvas { position: relative; width: 1200px; height: 576px; }
  .card {
    position: absolute;
    top: 138px;
    height: 294px;
    border-radius: 13px;
    box-shadow: var(--card-shadow);
  }
  .card--front {
    left: 82px;
    width: 484px;
    background: linear-gradient(180deg, #f4f4f4 0%, #e9e9e9 100%);
  }
  .card--back {
    left: 602px;
    width: 481px;
    background: linear-gradient(180deg, var(--brand-green) 0%, var(--brand-green) 55%, var(--brand-green-deep) 100%);
  }
  .holder-name {
    position: absolute;
    left: 36px;
    top: 36px;
    font-size: 21px;
    font-weight: 400;
    color: var(--ink);
    letter-spacing: 0.1px;
  }
  .holder-role {
    position: absolute;
    left: 36px;
    top: 66px;
    font-size: 11.5px;
    color: var(--ink-soft);
  }
  .contact-list {
    position: absolute;
    left: 36px;
    top: 98px;
    list-style: none;
    font-size: 12px;
    line-height: 17px;
    color: var(--ink-soft);
  }
  .contact-list .accent { color: var(--brand-green); }
  .brand {
    position: absolute;
    display: flex;
    align-items: center;
    gap: 16px;
  }
  .brand-dot {
    width: 22px;
    height: 22px;
    border-radius: 50%;
  }
  .brand-name {
    font-size: 24px;
    font-weight: 500;
    letter-spacing: 4px;
  }
  .card--front .brand { left: 36px; top: 218px; }
  .card--front .brand-dot { background: var(--brand-green); }
  .card--front .brand-name { color: var(--ink); }
  .card--back .brand { left: 259px; top: 214px; }
  .card--back .brand-dot { background: var(--ink); }
  .card--back .brand-name { color: var(--ink); }
</style>
</head>
<body>
<main class="canvas">
  <section class="card card--front" aria-label="Business card front">
    <h1 class="holder-name">Miro Halvensky, PhD</h1>
    <p class="holder-role">Roboticist | Vortalo Consulting</p>
    <ul class="contact-list">
      <li>318.570.9164</li>
      <li>miro@vortalo.com</li>
      <li>www.<span class="accent">vortalo</span>.com</li>
    </ul>
    <div class="brand">
      <span class="brand-dot"></span>
      <span class="brand-name">VORTALO</span>
    </div>
  </section>
  <section class="card card--back" aria-label="Business card back">
    <div class="brand">
      <span class="brand-dot"></span>
      <span class="brand-name">VORTALO</span>
    </div>
  </section>
</main>
</body>
</html>
```